Visitenkarten-Design für Goldankauf und Verkauf von Trauringen
Zielgruppe
Goldankauf und Verkauf von Trauringen
Aufgabenstellung
Edel, nicht zu bunt, das Design soll sich dem Kunden einprägen, ansprechend, gerne können auch Wasserzeichen verwendet werden.

```html
<!DOCTYPE html>
<html lang="de">
<head>
<meta charset="utf-8">
<title>Aurelia Ringhaus – Visitenkarten</title>
<link href="https://fonts.googleapis.com/css2?family=Cinzel:wght@400&family=Old+Standard+TT:wght@400&display=swap" rel="stylesheet">
<style>
  :root {
    --stage: #f2f2f2;
    --stage-light: #fbfbfb;
    --card-dark: #0c0c0c;
    --card-mid: #1b1b1b;
    --gold-light: #f7e68f;
    --gold-mid: #d6b552;
    --gold-deep: #a9802a;
    --gold-text: #e2c277;
    --ink-light: #f4f1ea;
  }
  * { margin: 0; padding: 0; box-sizing: border-box; }
  html, body { width: 1200px; height: 1200px; overflow: hidden; }
  body {
    background: radial-gradient(circle at 50% 45%, var(--stage-light) 0%, var(--stage) 70%, #e8e8e8 100%);
    position: relative;
    font-family: "Old Standard TT", Georgia, serif;
  }
  .card {
    position: absolute;
    top: 299px;
    width: 389px;
    height: 602px;
    overflow: hidden;
  }
  .card--front { left: 186px; }
  .card--back { left: 607px; }
  .card__surface {
    position: absolute;
    inset: 0;
    background: radial-gradient(ellipse at 50% 45%, var(--card-mid) 0%, var(--card-dark) 80%);
  }
  .gold-band {
    position: absolute;
    left: 0;
    width: 100%;
    height: 11px;
    background: linear-gradient(90deg, var(--gold-light) 0%, var(--gold-mid) 55%, var(--gold-deep) 100%);
  }
  .gold-band--top { top: 0; }
  .gold-band--bottom { bottom: 0; }

  .brand {
    position: absolute;
    left: 0;
    width: 100%;
    top: 268px;
    text-align: center;
  }
  .brand__name {
    font-family: "Cinzel", Georgia, serif;
    font-size: 29px;
    color: var(--gold-text);
    letter-spacing: 1px;
    line-height: 1;
  }
  .brand__dot {
    display: inline-block;
    width: 12px;
    height: 12px;
    border-radius: 50%;
    background: var(--gold-text);
    margin-right: 10px;
    vertical-align: 4px;
  }
  .brand__tagline {
    margin-top: 10px;
    font-size: 15px;
    color: var(--ink-light);
    letter-spacing: 0.5px;
  }

  .watermark {
    position: absolute;
    right: -90px;
    top: -60px;
    width: 300px;
    height: 300px;
    border-radius: 50%;
    background: radial-gradient(circle, rgba(140,120,60,0.55) 0%, rgba(110,90,40,0.35) 70%);
  }

  .owner {
    position: absolute;
    left: 25px;
    top: 223px;
  }
  .owner__name {
    font-family: "Cinzel", Georgia, serif;
    font-size: 30px;
    line-height: 28px;
    color: var(--gold-text);
    letter-spacing: -0.5px;
  }
  .owner__contact {
    margin-top: 8px;
    font-size: 15.5px;
    line-height: 21px;
    color: var(--ink-light);
  }
  .address {
    position: absolute;
    left: 25px;
    top: 485px;
    font-size: 16px;
    line-height: 21px;
    color: var(--ink-light);
  }
  .sep { color: var(--gold-mid); padding: 0 4px; }
</style>
</head>
<body>
  <section class="card card--front" aria-label="Vorderseite">
    <div class="card__surface" role="img" aria-label="Schwarze Ledertextur"></div>
    <div class="gold-band gold-band--top"></div>
    <div class="brand">
      <div class="brand__name"><span class="brand__dot"></span>Aurelia Ringhaus</div>
      <div class="brand__tagline">Goldankauf &amp; Trauringe</div>
    </div>
    <div class="gold-band gold-band--bottom"></div>
  </section>

  <section class="card card--back" aria-label="Rückseite">
    <div class="card__surface" role="img" aria-label="Schwarze Ledertextur"></div>
    <div class="watermark"></div>
    <div class="owner">
      <div class="owner__name">Inh. Lorena<br>Falkenrath</div>
      <div class="owner__contact">
        info@aurelia-ringhaus.de<br>
        Mobil: 06181-7730412
      </div>
    </div>
    <div class="address">
      Lindenhofer Gasse 12<span class="sep">•</span>63450 Hanau<br>
      Tel.: 06181-7730412<span class="sep">•</span>Fax: 06181-7730413<br>
      www.aurelia-ringhaus.de<br>
      info@aurelia-ringhaus.de
    </div>
    <div class="gold-band gold-band--bottom"></div>
  </section>
</body>
</html>
```